Brochure needed for 3D foam prop company

Looking for a designer to create a multi page brochure. Brochure will need to be able to be die cut so we're looking for something unique. The brochure needs to utilize our logo and the squares as possibly cut aways displaying imagery behind it for the front cover.

The brochure will feature the following sections:
- about us
- our process
- amazing clients
- anything is possible
Updates

So far we're still looking for an effective design that matches our requirements. It appears the die cutting element isn't being factored into the design (all except 1 design submitted has included this so far). Please read the brief and submit quality designs...so far we have not been very impressed.

Target Market(s)

Themeparks, water parks

Industry/Entity Type

Entertainment Industry

Font styles to use
Sans Serif

Requirements
Must have
• Logo, utilize our color theme

```html
<!DOCTYPE html>
<html lang="en">
<head>
<meta charset="utf-8">
<title>Novaform Props – Brochure Spread</title>
<link rel="stylesheet" href="https://fonts.googleapis.com/css2?family=Open+Sans:wght@400;700&display=swap">
<style>
  :root {
    --backdrop: #000000;
    --sky: #66ccf5;
    --paper: #ffffff;
    --sun: #f5e313;
    --tangerine: #f7941d;
    --ocean: #0b74c1;
    --ink: #111111;
    --brand: #1170bd;
    --rule: #bdbdbd;
  }
  html, body {
    margin: 0;
    padding: 0;
    width: 1200px;
    height: 999px;
    overflow: hidden;
    background: var(--backdrop);
  }
  .spread {
    position: relative;
    width: 1200px;
    height: 999px;
    font-family: "Open Sans", Arial, sans-serif;
    color: var(--ink);
  }
  .panel-art {
    position: absolute;
    left: 0;
    top: 0;
  }
  .cover {
    position: absolute;
    left: 330px;
    top: 153px;
    width: 542px;
    height: 703px;
    background: var(--paper);
    box-shadow: inset 0 0 0 1px var(--rule);
  }
  .brand-name {
    position: absolute;
    left: 0;
    right: 0;
    top: 522px;
    margin: 0;
    text-align: center;
    font-size: 44px;
    font-weight: 700;
    letter-spacing: -0.5px;
    color: var(--brand);
    line-height: 1;
  }
  .intro {
    position: absolute;
    top: 170px;
    width: 239px;
  }
  .intro h2 {
    margin: 0 0 6px;
    font-size: 14.5px;
    font-weight: 700;
    line-height: 1.2;
  }
  .intro p,
  .detail p {
    margin: 0;
    font-size: 9.4px;
    line-height: 12.7px;
    text-align: justify;
  }
  .intro--left { left: 83px; }
  .intro--right { left: 893px; }
  .detail {
    position: absolute;
    top: 689px;
    width: 168px;
  }
  .detail--left { left: 145px; }
  .detail--right { left: 897px; }
</style>
</head>
<body>
<main class="spread">
  <svg class="panel-art" width="1200" height="999" viewBox="0 0 1200 999" aria-hidden="true">
    <defs>
      <clipPath id="panel-clip">
        <rect x="58" y="153" width="272" height="703"/>
      </clipPath>
      <g id="side-panel">
        <rect x="58" y="153" width="272" height="703" fill="var(--sky)"/>
        <g clip-path="url(#panel-clip)">
          <polygon points="58,355 148,355 212,468 58,468" fill="var(--sun)"/>
          <polygon points="58,560 194,570 148,655 58,655" fill="var(--tangerine)"/>
          <polygon points="203,455 255,513 193,570 150,513" fill="var(--ocean)"/>
          <circle cx="83.7" cy="503.5" r="121.3" fill="var(--backdrop)"/>
          <polygon points="148,660 318,660 330,680 330,856 95,856 66,808" fill="var(--paper)"/>
        </g>
      </g>
    </defs>
    <use href="#side-panel"/>
    <use href="#side-panel" transform="translate(1203,0) scale(-1,1)"/>
  </svg>

  <section class="intro intro--left">
    <h2>What is Lorem Ipsum?</h2>
    <p>Lorem Ipsum is simply dummy text of the printing and typesetting industry. Lorem Ipsum has been the industry's standard dummy text ever since the 1500s, when an unknown printer took a galley of type and scrambled it to make a type specimen book. It has survived not only five centuries, but also the leap into electronic typesetting, remaining essentially unchanged. It was popularised in the 1960s with the release of Letraset sheets containing Lorem Ipsum passages, and more recently with desktop publishing software like Aldus PageMaker including versions of Lorem Ipsum.</p>
  </section>

  <section class="detail detail--left">
    <p>Lorem Ipsum is simply dummy text of the printing and typesetting industry. Lorem Ipsum has been the industry's standard dummy text ever since the 1500s, when an unknown printer took a galley of type and scrambled it to make a type specimen book. It has survived not only five centuries, but also the leap into electronic typesetting, remaining essentially unchanged.</p>
  </section>

  <section class="cover">
    <h1 class="brand-name">Novaform Props</h1>
  </section>

  <section class="intro intro--right">
    <h2>What is Lorem Ipsum?</h2>
    <p>Lorem Ipsum is simply dummy text of the printing and typesetting industry. Lorem Ipsum has been the industry's standard dummy text ever since the 1500s, when an unknown printer took a galley of type and scrambled it to make a type specimen book. It has survived not only five centuries, but also the leap into electronic typesetting, remaining essentially unchanged. It was popularised in the 1960s with the release of Letraset sheets containing Lorem Ipsum passages, and more recently with desktop publishing software like Aldus PageMaker including versions of Lorem Ipsum.</p>
  </section>

  <section class="detail detail--right">
    <p>Lorem Ipsum is simply dummy text of the printing and typesetting industry. Lorem Ipsum has been the industry's standard dummy text ever since the 1500s, when an unknown printer took a galley of type and scrambled it to make a type specimen book. It has survived not only five centuries, but also the leap into electronic typesetting, remaining essentially unchanged.</p>
  </section>
</main>
</body>
</html>
```